Corvane Electrical Solutions

On one side. LOGO (underneath:) Commercial Industrial Residential

- NAME & CONTACT DETAILS

Marcus T. Hollings
Project Manager

(Cell icon) (441) 582-6197
(Email icon) cvnelectricalsoultions@mailventra.com
(Facebook & Instagram icons )@cvnelectricalsolutions

Other side: LOGO - underneath ELECTRICAL CONSTRUCTION & MAINTENANCE . LED LIGHTING & AUTOMATION . LIFE SAFETY SYSTEMS (FIRE ALARM / SECURITY) . DATA & COMMUNICATION

```html
<!DOCTYPE html>
<html lang="en">
<head>
<meta charset="utf-8">
<title>Corvane Electrical Solutions – Business Card</title>
<link href="https://fonts.googleapis.com/css2?family=Lato:ital,wght@0,400;0,700;1,400;1,900&display=swap" rel="stylesheet">
<style>
  :root {
    --backdrop: #2a2a2a;
    --teal: #175a70;
    --teal-line: #7aa3b1;
    --white: #ffffff;
    --ink: #333a3e;
    --grey: #5b5f62;
  }
  * { margin: 0; padding: 0; box-sizing: border-box; }
  html, body { width: 1200px; height: 878px; overflow: hidden; }
  body {
    background: var(--backdrop);
    font-family: "Lato", sans-serif;
    position: relative;
  }
  .card {
    position: absolute;
    left: 320px;
    width: 560px;
    height: 320px;
    overflow: hidden;
  }
  .card--back { top: 92px; background: var(--teal); color: var(--white); }
  .card--front { top: 466px; background: var(--white); color: var(--ink); }

  /* back side */
  .back-brand {
    position: absolute; top: 66px; left: 0; width: 100%;
    display: flex; justify-content: center; align-items: center; gap: 14px;
  }
  .brand-mark { width: 16px; height: 16px; background: currentColor; }
  .brand-name {
    font-weight: 700; letter-spacing: 3px; text-transform: uppercase;
    font-size: 24px; line-height: 1.15;
  }
  .services {
    position: absolute; top: 170px; left: 0; width: 100%;
    list-style: none; text-align: center;
    font-size: 13px; letter-spacing: 0.6px; line-height: 24px; text-transform: uppercase;
  }

  /* front side */
  .person { position: absolute; top: 36px; left: 40px; }
  .person-name { font-weight: 900; font-style: italic; font-size: 28px; color: var(--teal); }
  .person-title { font-style: italic; font-size: 16px; color: var(--ink); margin-top: 2px; }

  .front-brand { position: absolute; top: 122px; right: 34px; text-align: right; color: var(--teal); }
  .front-brand .brand-line { display: flex; align-items: center; justify-content: flex-end; gap: 10px; }
  .front-brand .brand-name { font-size: 17px; letter-spacing: 2px; }
  .sectors {
    margin-top: 12px; font-size: 12px; font-weight: 700; letter-spacing: 0.8px;
    text-transform: uppercase; color: var(--teal);
  }
  .sectors span { margin: 0 6px; color: var(--ink); font-weight: 400; }

  .contacts { position: absolute; left: 40px; top: 200px; list-style: none; font-size: 17px; color: var(--ink); }
  .contacts li { display: flex; align-items: center; gap: 12px; height: 24px; }
  .contacts svg { width: 18px; height: 18px; fill: var(--teal); flex: none; }
  .rule { position: absolute; left: 40px; right: 34px; top: 258px; height: 1px; background: var(--teal-line); }
  .social { position: absolute; left: 40px; top: 268px; display: flex; align-items: center; gap: 8px; font-size: 17px; }
  .social-box { width: 16px; height: 16px; background: var(--teal); border-radius: 3px; }
  .social-handle { margin-left: 6px; }
  .band { position: absolute; left: 0; right: 0; bottom: 0; height: 12px; background: var(--teal); }
  .band-accent { position: absolute; left: 0; bottom: 0; width: 32px; height: 12px; background: var(--grey); }
</style>
</head>
<body>

<section class="card card--back" aria-label="Card back">
  <div class="back-brand">
    <span class="brand-mark"></span>
    <span class="brand-name">Corvane<br>Electrical<br>Solutions</span>
  </div>
  <ul class="services">
    <li>Electrical Construction &amp; Maintenance</li>
    <li>LED Lighting &amp; Automation</li>
    <li>Life Safety Systems (Fire Alarm / Security)</li>
    <li>Data &amp; Communication</li>
  </ul>
</section>

<section class="card card--front" aria-label="Card front">
  <div class="person">
    <h1 class="person-name">Marcus T. Hollings</h1>
    <p class="person-title">Project Manager</p>
  </div>

  <div class="front-brand">
    <div class="brand-line">
      <span class="brand-mark"></span>
      <span class="brand-name">Corvane Electrical Solutions</span>
    </div>
    <p class="sectors">Commercial<span>|</span>Industrial<span>|</span>Residential</p>
  </div>

  <ul class="contacts">
    <li>
      <svg viewBox="0 0 24 24" aria-hidden="true"><path d="M6.6 10.8c1.4 2.8 3.8 5.1 6.6 6.6l2.2-2.2c.3-.3.7-.4 1-.2 1.1.4 2.3.6 3.6.6.6 0 1 .4 1 1V20c0 .6-.4 1-1 1C10.6 21 3 13.4 3 4c0-.6.4-1 1-1h3.5c.6 0 1 .4 1 1 0 1.3.2 2.5.6 3.6.1.3 0 .7-.2 1L6.6 10.8z"/></svg>
      (441) 582-6197
    </li>
    <li>
      <svg viewBox="0 0 24 24" aria-hidden="true"><path d="M2 5h20v14H2V5zm2 2v.5l8 5 8-5V7H4zm0 2.8V17h16V9.8l-8 5-8-5z"/></svg>
      cvnelectricalsoultions@mailventra.com
    </li>
  </ul>
  <div class="rule"></div>
  <div class="social">
    <span class="social-box"></span>
    <span class="social-box"></span>
    <span class="social-handle">@cvnelectricalsolutions</span>
  </div>
  <div class="band"></div>
  <div class="band-accent"></div>
</section>

</body>
</html>
```